Poster

I have an animal hospital. I want a poster to hang in each exam room to show a picture of a normal sized heart and then an enlarged heart of a dog that was fed a grain-free diet. I want to warn people not to feed grain-free diets. Maybe at the top of the poster, "Do you feed grain-free?" and then the x-ray comparison, then the warnings of Canine Dilated Cardiomyopathy.

```html
<!DOCTYPE html>
<html lang="en">
<head>
<meta charset="utf-8">
<title>Do You Feed Grain-Free? – Exam Room Poster</title>
<link href="https://fonts.googleapis.com/css2?family=Barlow+Condensed:ital,wght@0,300;0,400;0,600;0,700;1,600;1,700&display=swap" rel="stylesheet">
<style>
  :root {
    --navy: #38398a;
    --red: #b22025;
    --coral: #e8565c;
    --green: #369436;
    --ink: #111111;
    --white: #ffffff;
  }
  * { margin: 0; padding: 0; box-sizing: border-box; }
  html, body { width: 810px; height: 1200px; overflow: hidden; background: var(--white); }
  .poster {
    position: relative;
    width: 810px;
    height: 1200px;
    overflow: hidden;
    background: var(--white);
    font-family: "Barlow Condensed", "Arial Narrow", sans-serif;
    color: var(--ink);
  }
  .artwork { position: absolute; left: 0; top: 0; width: 810px; height: 1200px; }

  .headline {
    position: absolute; left: 0; top: 36px; width: 100%;
    text-align: center;
    font-weight: 700; font-size: 58px; line-height: 1;
    color: var(--navy); letter-spacing: 0.3px;
  }
  .headline em { color: var(--red); font-style: italic; }

  .xray-label {
    position: absolute; font-weight: 400; font-size: 25px; line-height: 31px; color: var(--ink);
  }
  .xray-label--normal { left: 92px; top: 459px; }
  .xray-label--grainfree { left: 369px; top: 478px; }
  .xray-label em { font-style: italic; font-weight: 600; }

  .condition-band {
    position: absolute; left: 0; top: 577px; width: 810px; height: 198px;
    background: var(--navy); color: var(--white); text-align: center;
  }
  .condition-band h1 {
    margin-top: 30px;
    font-weight: 700; font-size: 48px; line-height: 1; letter-spacing: 0.4px;
  }
  .condition-band p {
    margin-top: 14px;
    font-weight: 400; font-size: 33px; line-height: 42px;
  }
  .condition-band strong { color: var(--coral); font-style: italic; font-weight: 700; }

  .dog-photo {
    position: absolute; left: 62px; top: 812px; width: 514px; height: 212px;
    background: radial-gradient(ellipse at 55% 55%, #a8552b 0%, #b9693a 35%, rgba(220,170,130,0.4) 62%, rgba(255,255,255,0) 75%);
  }
  .signs-label {
    position: absolute; left: 63px; top: 818px;
    font-weight: 400; font-size: 25px; color: var(--ink);
  }
  .signs-list {
    position: absolute; right: 48px; top: 826px; list-style: none; text-align: right;
    font-weight: 400; font-size: 26px; line-height: 34px; color: var(--ink);
  }

  .call-to-action {
    position: absolute; left: 37px; top: 1060px;
    font-weight: 300; font-size: 49px; line-height: 58px; color: var(--navy);
    letter-spacing: -0.5px;
  }
  .call-to-action b { font-weight: 700; }
  .call-to-action .cta-heart { color: var(--red); font-weight: 700; }
  .call-to-action .cta-check { color: var(--green); font-weight: 700; }
</style>
</head>
<body>
<main class="poster">
  <svg class="artwork" viewBox="0 0 1569 2324" aria-hidden="false">
    <defs>
      <linearGradient id="xrayTone" x1="0" y1="0" x2="1" y2="1">
        <stop offset="0" stop-color="#1a1a1a"/>
        <stop offset="0.35" stop-color="#8f8f8f"/>
        <stop offset="0.6" stop-color="#c9c9c9"/>
        <stop offset="1" stop-color="#7a7a7a"/>
      </linearGradient>
      <radialGradient id="xrayToneLarge" cx="0.5" cy="0.55" r="0.6">
        <stop offset="0" stop-color="#d6d6d6"/>
        <stop offset="0.6" stop-color="#a8a8a8"/>
        <stop offset="1" stop-color="#0c0c0c"/>
      </radialGradient>
      <clipPath id="clipNormal">
        <path d="M497 937 L160 600 A185 185 0 0 1 483 400 A185 185 0 0 1 838 600 Z"/>
      </clipPath>
      <clipPath id="clipGrainFree">
        <path d="M1112 1032 L770 690 A190 190 0 0 1 1098 540 A190 190 0 0 1 1470 690 Z"/>
      </clipPath>
    </defs>

    <!-- normal heart frame -->
    <g class="heart-normal">
      <path fill="var(--green)" d="M497 937 L160 600 A185 185 0 0 1 483 400 A185 185 0 0 1 838 600 Z" transform="translate(0,-120)"/>
      <g clip-path="url(#clipNormal)">
        <rect x="100" y="300" width="760" height="650" fill="url(#xrayTone)" role="img" aria-label="Chest x-ray of a dog with a normal sized heart"/>
      </g>
    </g>

    <!-- enlarged heart frame -->
    <g class="heart-grainfree">
      <path fill="var(--red)" d="M1112 1032 L770 690 A190 190 0 0 1 1098 540 A190 190 0 0 1 1470 690 Z" transform="translate(0,-120)"/>
      <g clip-path="url(#clipGrainFree)">
        <rect x="720" y="400" width="780" height="640" fill="url(#xrayToneLarge)" role="img" aria-label="Chest x-ray of a dog on a grain-free diet showing an enlarged heart"/>
      </g>
    </g>

    <!-- small outline heart -->
    <path class="icon-heart" fill="none" stroke="var(--green)" stroke-width="9" stroke-linejoin="round"
          d="M164 852 L96 784 A42 42 0 0 1 164 740 A42 42 0 0 1 232 784 Z"/>

    <!-- no-grain icon -->
    <g class="icon-no-grain" stroke="var(--red)" fill="none">
      <circle cx="1412" cy="908" r="82" stroke-width="13"/>
      <line x1="1355" y1="851" x2="1470" y2="966" stroke-width="13"/>
      <g fill="var(--red)" stroke="none">
        <rect x="1404" y="870" width="7" height="82" transform="rotate(20 1407 911)"/>
        <ellipse cx="1400" cy="885" rx="8" ry="15" transform="rotate(-30 1400 885)"/>
        <ellipse cx="1425" cy="893" rx="8" ry="15" transform="rotate(40 1425 893)"/>
        <ellipse cx="1393" cy="908" rx="8" ry="15" transform="rotate(-40 1393 908)"/>
        <ellipse cx="1418" cy="917" rx="8" ry="15" transform="rotate(40 1418 917)"/>
        <ellipse cx="1388" cy="930" rx="8" ry="15" transform="rotate(-45 1388 930)"/>
      </g>
    </g>

    <!-- hand-style heart accent -->
    <path class="accent-heart" fill="none" stroke="var(--red)" stroke-width="14" stroke-linecap="round" stroke-linejoin="round"
          d="M1392 2110 C1350 1990 1280 1950 1282 2040 C1285 2120 1340 2180 1368 2245 C1420 2190 1500 2110 1512 2020 C1522 1945 1450 1950 1392 2110"/>
  </svg>

  <h2 class="headline">DO YOU FEED <em>GRAIN-FREE</em>?</h2>

  <p class="xray-label xray-label--normal">Normal heart</p>
  <p class="xray-label xray-label--grainfree">Heart of a dog<br>on a <em>grain-free diet</em></p>

  <section class="condition-band">
    <h1>CANINE DILATED CARDIOMYOPATHY</h1>
    <p>is a <strong>serious</strong> and <strong>often fatal</strong> condition<br>in dogs caused by a grain-free diet</p>
  </section>

  <div class="dog-photo" role="img" aria-label="Photo of a tired brown dog lying down on a white floor"></div>
  <p class="signs-label">SIGNS:</p>
  <ul class="signs-list">
    <li>increased breathing rate, excess panting</li>
    <li>reduced exercise ability, tiring quickly</li>
    <li>coughing or gagging</li>
    <li>restless sleeping</li>
  </ul>

  <p class="call-to-action">KEEP YOUR LOVED DOGS <b>HEALTHY</b><br>AND GET THEIR <span class="cta-heart">HEART</span> <span class="cta-check">CHECKED</span> TODAY!</p>
</main>
</body>
</html>
```